Boring Fiberglass Repair Company needs creative business cards

The Fiberglass Repair industry isn't very fun or creative but we'd like a business card that communicates a fresh, modern, and service-oriented feel. We repair bathroom fixtures (bath tubs, showers, etc) which are made out of fiberglass. Our fiberglass repair service will be sold to bathtub manufacturers and also businesses that sell bathtubs. We will also offer our services to home owners that have broken showers and bathtubs.
Target Market(s)
Home builders, plumbing wholesalers, home owners
Contact Information for Business Card
Name
Phone Number
Email Address
Business Address
Tag line: "Quality Craftsmanship Today"

```html
<!DOCTYPE html>
<html lang="en">
<head>
<meta charset="utf-8">
<title>Harbor Line Fiberglass – Business Cards</title>
<link rel="stylesheet" href="https://fonts.googleapis.com/css2?family=Montserrat:wght@400;500;600;700;900&display=swap">
<style>
  :root {
    --navy: #0b2257;
    --red: #e31e2a;
    --white: #ffffff;
    --ink: #3a3f4a;
    --stage: #1d1e22;
  }
  * { margin: 0; padding: 0; box-sizing: border-box; }
  html, body { width: 1200px; height: 786px; overflow: hidden; }
  body {
    background: var(--stage);
    font-family: "Montserrat", Arial, sans-serif;
    position: relative;
  }
  .card {
    position: absolute;
    top: 245px;
    width: 520px;
    height: 297px;
    overflow: hidden;
  }
  .card--front { left: 60px; background: var(--white); }
  .card--back { left: 620px; background: var(--navy); }

  .card__bands { position: absolute; inset: 0; }
  .brand {
    position: absolute;
    display: flex;
    align-items: center;
    gap: 8px;
    font-weight: 900;
    text-transform: uppercase;
    line-height: 1;
    white-space: nowrap;
  }
  .brand__mark { width: 10px; height: 10px; background: var(--red); flex: none; }

  /* front */
  .card--front .brand { left: 30px; top: 104px; color: var(--navy); font-size: 16px; letter-spacing: 0.4px; }
  .person { position: absolute; right: 34px; top: 40px; text-align: right; }
  .person__name { font-size: 21px; font-weight: 700; color: var(--navy); letter-spacing: 0.3px; text-transform: uppercase; white-space: nowrap; }
  .person__name .surname { color: var(--red); }
  .person__role { font-size: 12px; color: var(--ink); margin-top: 2px; }
  .address { position: absolute; right: 34px; top: 176px; text-align: right; font-size: 11.5px; color: var(--ink); line-height: 1.45; }
  .contacts { position: absolute; left: 44px; top: 176px; list-style: none; font-size: 11.5px; color: var(--ink); line-height: 1.5; }
  .contacts li { display: flex; align-items: center; gap: 7px; white-space: nowrap; }
  .contacts svg { width: 9px; height: 9px; flex: none; }
  .contacts .accent { color: var(--navy); font-weight: 600; }

  /* back */
  .card--back .brand {
    left: 0; right: 0; top: 132px;
    justify-content: center;
    color: var(--white);
    font-size: 27px;
    letter-spacing: 0.8px;
  }
  .card--back .brand__mark { width: 13px; height: 13px; }
  .tagline {
    position: absolute; left: 0; right: 0; bottom: 38px;
    display: flex; align-items: center; justify-content: center; gap: 14px;
    color: var(--white); font-size: 12.5px; font-weight: 500; letter-spacing: 0.6px; text-transform: uppercase;
  }
  .tagline__rule { width: 110px; height: 1px; background: var(--red); }
</style>
</head>
<body>

<section class="card card--front">
  <svg class="card__bands" viewBox="0 0 520 297" preserveAspectRatio="none" aria-hidden="true">
    <rect x="498" y="0" width="22" height="22" fill="var(--navy)"/>
    <line x1="40" y1="162" x2="290" y2="162" stroke="var(--red)" stroke-width="1"/>
    <line x1="290" y1="162" x2="486" y2="162" stroke="var(--navy)" stroke-width="1"/>
    <polygon points="0,289 318,289 318,297 0,297" fill="var(--red)"/>
    <polygon points="318,297 326,242 520,242 520,297" fill="var(--navy)"/>
  </svg>

  <div class="brand"><span class="brand__mark"></span><span>Harbor Line Fiberglass</span></div>

  <div class="person">
    <p class="person__name">Daniel <span class="surname">Reeve</span></p>
    <p class="person__role">Founder</p>
  </div>

  <p class="address">27 Marsh Lane,<br>Eastfield VIC 3999, Australia</p>

  <ul class="contacts">
    <li><svg viewBox="0 0 10 10"><path d="M2 1l2 2-1 1.2c.6 1.2 1.5 2.1 2.7 2.7L7 6l2 2-1.3 1.3C4.5 9 1 5.5.7 2.3z" fill="var(--red)"/></svg><span>(03) 5550 1847</span></li>
    <li><svg viewBox="0 0 10 10"><rect x="1" y="2" width="8" height="6" fill="none" stroke="var(--red)" stroke-width="1.1"/><path d="M1 2l4 3.5L9 2" fill="none" stroke="var(--red)" stroke-width="1.1"/></svg><span>info@harborline.com</span></li>
    <li><svg viewBox="0 0 10 10"><circle cx="5" cy="5" r="4" fill="none" stroke="var(--red)" stroke-width="1.1"/><path d="M1 5h8M5 1c-2 2.5-2 5.5 0 8M5 1c2 2.5 2 5.5 0 8" fill="none" stroke="var(--red)" stroke-width="0.8"/></svg><span>www.<span class="accent">harborline</span>.com</span></li>
  </ul>
</section>

<section class="card card--back">
  <div class="brand"><span class="brand__mark"></span><span>Harbor Line Fiberglass</span></div>
  <p class="tagline"><span class="tagline__rule"></span>Quality Craftsmanship Today<span class="tagline__rule"></span></p>
</section>

</body>
</html>
```